Letterhead for 3 attorney Workers' Comp law firm

We are a 3 attorney law office. We specialize in Workers' Compensation. Our office represents workers who are injured on the job, and the estates of workers who are killed one the job.
When we started our office, we created our own letterhead & have been using it for years. We've just recently hired the 3rd attorney, and were going to just add his name to the letterhead, but have decided we wanted to get a professionally designed letterhead and business cards at this point.
We want something that looks clean and professional. It must look good in black and white because we often make multiple copies of our documents. We're hoping for a design that resonates confidence, reliability and experience.
The design must include the firm name: Dorrance & Pike, PLLC. We would like the PLLC to be small compared to the Dorrance & Pike graphic. We also want to incorporate the attorney names: Ulric Dorrance, Janet Pike, and Lyle Hagberg. Our current letterhead has our contact info in the footer at the bottom of the page. We like that design, but are open to the idea of having it at the top. We'll leave that at the discretion of the designer. Our contact info is as follows: 472 S. Larchmont Avenue, Suite 315 Bellingham, WA 98117 Phone: 360-514-2967, Fax: 360-521-6079, and our website: www.dorrancepike-law.example
Target Market(s)
Clients, courts, other legal offices, doctors offices. These are the people who see our letterhead most frequently. It's not so much for marketing purposes, mainly so that we have a professional image when sending out documents.
Industry/Entity Type
Law Firm
Contact Information for Business Card
On the back of the business card: it can be designed, or be a template for filling in appointment reminder information (i.e. date, time, etc)
Colors
Designer to choose colors to be used in the design.
Requirements
Must have
- Must have our firm name at the top.
- Must include the attorney names.
- Must have all of our contact information (can be at top or bottom - whatever looks best with the design)
Nice to have
- A strong, confident design
Should not have
- We don't want the design to be playful, cartoony or busy.

```html
<!DOCTYPE html>
<html lang="en">
<head>
<meta charset="utf-8">
<title>Dorrance &amp; Pike, PLLC — Letterhead</title>
<link rel="stylesheet" href="https://fonts.googleapis.com/css2?family=Questrial&family=Source+Sans+3:wght@600&family=Arimo:ital,wght@1,700&display=swap">
<style>
  :root {
    --paper: #ffffff;
    --ink: #1a1a1a;
    --trim: #9a9a9a;
  }
  html, body {
    margin: 0;
    padding: 0;
    overflow: hidden;
    background: var(--paper);
  }
  .letterhead {
    position: relative;
    width: 874px;
    height: 1200px;
    background: var(--paper);
    color: var(--ink);
    overflow: hidden;
  }
  .crop-marks {
    position: absolute;
    inset: 0;
  }
  .firm-header {
    position: absolute;
    left: 57px;
    top: 64px;
  }
  .firm-name {
    margin: 0;
    font-family: "Questrial", sans-serif;
    font-weight: 400;
    font-size: 40px;
    line-height: 1;
    letter-spacing: 0.5px;
    color: var(--ink);
  }
  .attorney-names {
    margin: 10px 0 0;
    width: 240px;
    text-align: center;
    font-family: "Arimo", sans-serif;
    font-style: italic;
    font-weight: 700;
    font-size: 8.5px;
    line-height: 1.3;
    color: var(--ink);
  }
  .attorney-names .title {
    display: block;
  }
  .footer {
    position: absolute;
    left: 61px;
    right: 58px;
    top: 1086px;
    border-top: 1.5px solid var(--ink);
    padding-top: 9px;
    font-family: "Source Sans 3", sans-serif;
    font-weight: 600;
    font-size: 11.6px;
    letter-spacing: -0.25px;
    white-space: nowrap;
    color: var(--ink);
  }
</style>
</head>
<body>
  <div class="letterhead">
    <svg class="crop-marks" width="874" height="1200" viewBox="0 0 874 1200" aria-hidden="true">
      <g stroke="var(--trim)" stroke-width="1">
        <line x1="44" y1="0" x2="44" y2="27"/>
        <line x1="0" y1="43" x2="27" y2="43"/>
        <line x1="830" y1="0" x2="830" y2="27"/>
        <line x1="847" y1="43" x2="874" y2="43"/>
        <line x1="0" y1="1159" x2="27" y2="1159"/>
        <line x1="44" y1="1174" x2="44" y2="1200"/>
        <line x1="847" y1="1159" x2="874" y2="1159"/>
        <line x1="830" y1="1174" x2="830" y2="1200"/>
      </g>
    </svg>

    <header class="firm-header">
      <h1 class="firm-name">Dorrance &amp; Pike, PLLC</h1>
      <p class="attorney-names">
        Ulric Dorrance, Janet Pike &amp; Lyle Hagberg
        <span class="title">Attorneys</span>
      </p>
    </header>

    <footer class="footer">
      472 S. Larchmont Avenue, Suite 315 Bellingham, WA 98117 | Phone: 360-514-2967, Fax: 360-521-6079, | website: www.dorrancepike-law.example
    </footer>
  </div>
</body>
</html>
```